Brio 41 specialty coffee shop business card

Please use Design #5812047 from previous project (logo design). Brio 41 is a new coffee shop that will serve specialty coffee and will focus on high quality products. I would like to use orange and brown colors. I like designs that are simple but elegant and that deliver a message that is easy to recognize. I will upload a file of the logo design.

Industry/Entity Type

Coffee Shop

Contact Information for Business Card

Leon Cordravik
(555) 203-7719

Font styles to use
Serif
Sans Serif
Script

Requirements
Must have
• simple and elegant, colors match nicely, I like to use orange and brown. Background creme color.
Should not have
• complex designs that are hard to understand.

```html
<!DOCTYPE html>
<html lang="en">
<head>
<meta charset="utf-8">
<title>Brio 41 – Business Card</title>
<link rel="stylesheet" href="https://fonts.googleapis.com/css2?family=Allura&family=Open+Sans:wght@400&family=Montserrat:wght@400&display=swap">
<style>
  :root {
    --page-bg: #e9e4de;
    --card-creme: #f5eee5;
    --coffee-brown: #43281c;
    --gold: #a88660;
    --gold-light: #c9a77c;
    --ink: #3a2419;
    --owner-grey: #4a3f39;
  }
  * { margin: 0; padding: 0; box-sizing: border-box; }
  html, body {
    width: 1200px;
    height: 970px;
    overflow: hidden;
    background: var(--page-bg);
  }
  .business-card {
    position: absolute;
    left: 172px;
    top: 270px;
    width: 856px;
    height: 475px;
    background: var(--card-creme);
    border-radius: 3px;
    overflow: hidden;
    box-shadow: 0 10px 30px rgba(60, 40, 25, 0.18);
  }
  .card-wave {
    position: absolute;
    inset: 0;
    width: 856px;
    height: 475px;
  }
  .brand-lockup {
    position: absolute;
    left: 72px;
    top: 170px;
    display: flex;
    align-items: center;
    gap: 18px;
  }
  .brand-dot {
    width: 46px;
    height: 46px;
    border-radius: 50%;
    background: var(--gold);
  }
  .brand-name {
    font-family: "Montserrat", sans-serif;
    font-weight: 400;
    font-size: 58px;
    line-height: 1;
    color: var(--coffee-brown);
  }
  .holder-name {
    position: absolute;
    right: 33px;
    top: 58px;
    font-family: "Allura", cursive;
    font-size: 40px;
    line-height: 1;
    color: var(--ink);
  }
  .holder-role {
    position: absolute;
    right: 32px;
    top: 110px;
    font-family: "Open Sans", sans-serif;
    font-size: 19px;
    line-height: 1.2;
    color: var(--owner-grey);
  }
  .contact-phone {
    position: absolute;
    right: 47px;
    top: 386px;
    font-family: "Montserrat", sans-serif;
    font-size: 26px;
    line-height: 1.2;
    letter-spacing: 0.5px;
    color: var(--gold-light);
  }
</style>
</head>
<body>
  <div class="business-card">
    <svg class="card-wave" viewBox="0 0 856 475" aria-hidden="true">
      <path d="M0,425 C200,440 380,445 500,400 C640,340 740,240 856,218 L856,475 L0,475 Z" fill="var(--coffee-brown)"/>
      <path d="M0,370 C180,405 360,430 490,385 C630,330 740,225 856,205" fill="none" stroke="var(--gold)" stroke-width="7"/>
      <path d="M0,405 C190,428 370,440 495,395 C635,338 742,232 856,212" fill="none" stroke="var(--gold)" stroke-width="3" opacity="0.8"/>
    </svg>
    <div class="brand-lockup">
      <span class="brand-dot"></span>
      <span class="brand-name">Brio 41</span>
    </div>
    <div class="holder-name">Leon Cordravik</div>
    <div class="holder-role">owner</div>
    <div class="contact-phone">(555) 203-7719</div>
  </div>
</body>
</html>
```